Bramwell Business Cards

Logo files are included. Full "Bramwell" logo should be included on the back of the business card. The B symbol should be included on the front with the contact information.

Bramwell, LLC is the company name and we do commercial construction and real estate development consulting services. Look for a fairly simple card design utilizing our logo.

```html
<!DOCTYPE html>
<html lang="en">
<head>
<meta charset="utf-8">
<title>Bramwell Business Cards</title>
<link href="https://fonts.googleapis.com/css2?family=Montserrat:wght@400;500;700&display=swap" rel="stylesheet">
<style>
  :root {
    --navy: #1b3a52;
    --gold: #eeae1e;
    --paper: #ffffff;
    --stage: #ececec;
    --map: #ececee;
  }
  * { box-sizing: border-box; margin: 0; padding: 0; }
  html, body { width: 1187px; height: 1200px; overflow: hidden; }
  body {
    background: var(--stage);
    font-family: "Montserrat", sans-serif;
    color: var(--navy);
    position: relative;
  }
  .card {
    position: absolute;
    left: 113px;
    width: 960px;
    height: 546px;
    background: var(--paper);
    overflow: hidden;
    box-shadow: 0 6px 18px rgba(0,0,0,0.18);
  }
  .card--back { top: 34px; }
  .card--front { top: 620px; }
  .card__topline {
    position: absolute; left: 0; top: 0; width: 100%; height: 13px;
    background: var(--gold);
  }
  .card__footer {
    position: absolute; left: 0; bottom: 0; width: 100%; height: 67px;
    background: var(--navy);
    color: var(--gold);
    font-size: 22px; font-weight: 500;
    display: flex; align-items: center; justify-content: center;
    z-index: 3;
  }
  .world-map {
    position: absolute; left: 100px; top: 90px; width: 780px; height: 370px;
    background: radial-gradient(ellipse at center, var(--map) 0%, rgba(236,236,238,0.6) 55%, rgba(255,255,255,0) 75%);
    z-index: 0;
  }

  /* Back: wordmark */
  .wordmark {
    position: absolute; left: 0; width: 100%; top: 160px;
    display: flex; flex-direction: column; align-items: center; gap: 22px;
    z-index: 2;
  }
  .wordmark__circle {
    width: 150px; height: 150px; border-radius: 50%;
    border: 8px solid var(--navy);
  }
  .wordmark__name {
    font-size: 86px; font-weight: 500; letter-spacing: 1px;
    text-transform: uppercase; color: var(--navy); line-height: 1;
  }

  /* Front: person and contacts */
  .person { position: absolute; left: 64px; top: 78px; z-index: 2; }
  .person__name { font-size: 44px; line-height: 1; }
  .person__first { font-weight: 700; }
  .person__last { font-weight: 400; }
  .person__role { font-size: 27px; margin-top: 6px; }
  .person__rule {
    position: absolute; left: 0; top: 183px; width: 407px; height: 2px;
    background: var(--navy); z-index: 2;
  }
  .contacts {
    position: absolute; left: 64px; top: 228px; list-style: none; z-index: 2;
  }
  .contacts li {
    display: flex; align-items: center; gap: 12px;
    font-size: 24px; height: 46px;
  }
  .contacts svg { width: 20px; height: 20px; flex: none; }
  .brand-seal {
    position: absolute; left: 570px; top: 106px; width: 300px; height: 300px;
    border-radius: 50%; border: 10px solid var(--navy);
    display: flex; align-items: center; justify-content: center;
    z-index: 2;
  }
  .brand-seal__name { font-size: 44px; font-weight: 500; color: var(--navy); }
</style>
</head>
<body>

<section class="card card--back">
  <div class="card__topline"></div>
  <div class="world-map" role="img" aria-label="Faint dotted world map in light grey"></div>
  <div class="wordmark">
    <div class="wordmark__circle"></div>
    <div class="wordmark__name">Bramwell</div>
  </div>
  <div class="card__footer">www.bramwellco.com</div>
</section>

<section class="card card--front">
  <div class="card__topline"></div>
  <div class="world-map" role="img" aria-label="Faint dotted world map in light grey"></div>

  <div class="person">
    <div class="person__name"><span class="person__first">Daniel</span> <span class="person__last">Reyes</span></div>
    <div class="person__role">Director</div>
  </div>
  <div class="person__rule"></div>

  <ul class="contacts">
    <li>
      <svg viewBox="0 0 20 20" aria-hidden="true"><rect x="5" y="1.5" width="10" height="17" rx="2" fill="none" stroke="var(--navy)" stroke-width="2"/><circle cx="10" cy="15" r="1.2" fill="var(--navy)"/></svg>
      +000 555 0142
    </li>
    <li>
      <svg viewBox="0 0 20 20" aria-hidden="true"><path d="M4 2 L7.5 2 L9 6 L7 7.5 Q9 12 12.5 13 L14 11 L18 12.5 L18 16 Q17 18 14.5 18 Q5 16 2 5.5 Q2 3 4 2 Z" fill="none" stroke="var(--navy)" stroke-width="1.6" stroke-linejoin="round"/></svg>
      +000 555 0143
    </li>
    <li>
      <svg viewBox="0 0 20 20" aria-hidden="true"><rect x="2" y="4.5" width="16" height="11" rx="1" fill="none" stroke="var(--navy)" stroke-width="1.8"/><path d="M2.5 5 L10 11 L17.5 5" fill="none" stroke="var(--navy)" stroke-width="1.8"/></svg>
      info@bramwellco.com
    </li>
    <li>
      <svg viewBox="0 0 20 20" aria-hidden="true"><circle cx="10" cy="10" r="8" fill="none" stroke="var(--navy)" stroke-width="1.6"/><ellipse cx="10" cy="10" rx="3.5" ry="8" fill="none" stroke="var(--navy)" stroke-width="1.4"/><path d="M2 10 H18 M3.5 6 H16.5 M3.5 14 H16.5" stroke="var(--navy)" stroke-width="1.4"/></svg>
      www.bramwellco.com
    </li>
    <li>
      <svg viewBox="0 0 20 20" aria-hidden="true"><path d="M10 19 Q4 11.5 4 7.5 A6 6 0 0 1 16 7.5 Q16 11.5 10 19 Z" fill="var(--navy)"/><circle cx="10" cy="7.5" r="2.2" fill="#fff"/></svg>
      18 Alder Ridge Road, Larkfield, MT 59001
    </li>
  </ul>

  <div class="brand-seal"><span class="brand-seal__name">Bramwell</span></div>

  <div class="card__footer">Commercial Construction and Real Estate Development Consulting Services</div>
</section>

</body>
</html>
```